Business Card Design

Electronic Security
Alarm Systems
CCTV
Electronic Access Control
Security System Integration

Industry/Entity Type

Business

Contact Information for Business Card

Gareth Linwood
PO Box 862
Yarrowdale Qld 4173
Phone 07 38265140
Mob 0428637291

```html
<!DOCTYPE html>
<html lang="en">
<head>
<meta charset="utf-8">
<title>Business Card – Gareth Linwood</title>
<link rel="stylesheet" href="https://fonts.googleapis.com/css2?family=Arimo:wght@400;700&display=swap">
<style>
  :root {
    --page-bg: #ececec;
    --card-bg: #ffffff;
    --ink: #111111;
    --divider: #5a4a44;
    --brand: #1f8fcf;
    --shadow: rgba(0, 0, 0, 0.12);
  }
  * { box-sizing: border-box; margin: 0; padding: 0; }
  html, body {
    width: 1200px;
    height: 864px;
    overflow: hidden;
    background: var(--page-bg);
    font-family: "Arimo", Arial, sans-serif;
    color: var(--ink);
  }
  .canvas {
    position: relative;
    width: 1200px;
    height: 864px;
  }
  .card {
    position: absolute;
    left: 150px;
    top: 157px;
    width: 900px;
    height: 550px;
    background: var(--card-bg);
    box-shadow: 0 6px 24px var(--shadow);
  }
  .brand-panel {
    position: absolute;
    left: 0;
    top: 0;
    width: 400px;
    height: 100%;
    display: flex;
    align-items: center;
    justify-content: center;
    padding-top: 60px;
  }
  .brand {
    display: flex;
    align-items: center;
    gap: 14px;
  }
  .brand-mark {
    width: 22px;
    height: 22px;
    background: var(--brand);
  }
  .brand-name {
    font-size: 30px;
    font-weight: 400;
    color: var(--brand);
    letter-spacing: 0.5px;
  }
  .divider {
    position: absolute;
    left: 400px;
    top: 40px;
    width: 1px;
    height: 400px;
    background: var(--divider);
  }
  .details {
    position: absolute;
    left: 450px;
    top: 0;
    right: 40px;
    height: 100%;
  }
  .person-name {
    position: absolute;
    top: 62px;
    font-size: 30px;
    font-weight: 700;
  }
  .contact-list {
    position: absolute;
    top: 300px;
    list-style: none;
  }
  .contact-item {
    display: flex;
    align-items: center;
    gap: 16px;
    font-size: 24px;
    line-height: 36px;
    white-space: nowrap;
  }
  .contact-icon {
    width: 20px;
    height: 22px;
    flex: none;
  }
</style>
</head>
<body>
<main class="canvas">
  <article class="card">
    <section class="brand-panel">
      <div class="brand">
        <span class="brand-mark"></span>
        <span class="brand-name">Brightwall Security</span>
      </div>
    </section>

    <div class="divider"></div>

    <section class="details">
      <h1 class="person-name">Gareth Linwood</h1>
      <ul class="contact-list">
        <li class="contact-item">
          <svg class="contact-icon" viewBox="0 0 20 22" aria-hidden="true">
            <rect x="4" y="2" width="12" height="18" rx="2" fill="none" stroke="#111" stroke-width="2.4"/>
            <rect x="8" y="16" width="4" height="1.6" fill="#111"/>
          </svg>
          <span>0428637291</span>
        </li>
        <li class="contact-item">
          <svg class="contact-icon" viewBox="0 0 20 22" aria-hidden="true">
            <path d="M5 4 L8 4 L9.5 8 L7.5 9.6 C8.6 12 10.2 13.6 12.4 14.6 L14 12.6 L18 14 L18 17 C18 18 17 19 16 19 C9.5 18.5 4.5 13.5 4 7 C4 5 4.5 4 5 4 Z" fill="#111"/>
          </svg>
          <span>07 38265140</span>
        </li>
        <li class="contact-item">
          <svg class="contact-icon" viewBox="0 0 20 22" aria-hidden="true">
            <path d="M10 1.5 C5.6 1.5 3 4.6 3 8.2 C3 12.8 10 20.5 10 20.5 C10 20.5 17 12.8 17 8.2 C17 4.6 14.4 1.5 10 1.5 Z" fill="none" stroke="#111" stroke-width="2.2"/>
            <circle cx="10" cy="8.2" r="2.4" fill="#111"/>
          </svg>
          <span>PO Box 862 Yarrowdale Qld 4173</span>
        </li>
      </ul>
    </section>
  </article>
</main>
</body>
</html>
```